Process infographic

Introducing Tessa – the virtual restaurant experience at home

Missing going out on dining at your favourite restaurant with your friends, then Tessa Dining is the answer.

While it may not be possible during the COVID-19 pandemic, or when restaurants return as booking opportunities will be hard to get, an innovative new concept gives people the chance to enjoy a virtual restaurant experience at home.

TESSA offers diners the ability to get the restaurant experience at home and restaurants to expand their dining rooms beyond the confines of social distancing

Tessa Dining is an app where you can book your favourite restaurant table, invite your friends and choose your menu and beverages. On the day the restaurant will come to your house, set your table, cook and serve you the menu you have chosen, serve you drinks and clean up, just like you where at the restaurant.

We are looking for 2 similar infographics to explain a process from 2 different perspective

The design needs to be simple, contemporary, imaginative and modern for this concept, it needs to be sophisticated, something that would represent an up-market to fine dining style of restaurant. The designs need to be easily understood using white space to separate the elements

Our preferred colour is attached along with our logos

Infographic 1 - Host Process
1. Host makes reservation at favourite restaurant at home on the Tessa Dining App
2. Select menus and invite guests
3. Confirm either single or shared payment options
4. Booking confirmed with restaurant
5. Host confirms on the App they the required equipment
6. Cook/server arrive 1 hour prior to guests, prepares and sets table
7. Guests arrive and cook/server offer dinks and serves meal
8. Cook/Server cleans up and finalises check with host

Infographic 2 - Restaurant Process
1. Host makes reservation and orders meal
2. Restaurant confirm reservation details
3. Restaurant prepares cuisine and arranges cook/serve waiter
4. Cook/server arrive 1 hour before guests, prepares and sets table
5. Cook/server cooks and serves meals and wine
6. Cook/Server cleans up and finalises check with host

Good Luck

```html
<!DOCTYPE html>
<html lang="en">
<head>
<meta charset="utf-8">
<title>Tessa Dining – Restaurant Process</title>
<link href="https://fonts.googleapis.com/css2?family=Montserrat:wght@700;800&family=Arimo:wght@400;700&display=swap" rel="stylesheet">
<style>
  :root {
    --bg: #000000;
    --plum: #7a1b6b;
    --plum-soft: #8e3580;
    --ink: #ffffff;
  }
  * { margin: 0; padding: 0; box-sizing: border-box; }
  html, body { width: 1200px; height: 842px; overflow: hidden; background: var(--bg); }
  .canvas { position: relative; width: 1200px; height: 842px; background: var(--bg); color: var(--ink); }

  .brand { position: absolute; left: 0; right: 0; top: 104px; text-align: center;
    font-family: "Montserrat", sans-serif; font-weight: 800; color: var(--ink); }
  .brand-dot { display: block; width: 34px; height: 34px; margin: 0 auto 12px; border-radius: 50%; background: var(--ink); }
  .brand-name { display: block; font-size: 24px; letter-spacing: 10px; padding-left: 10px; line-height: 1; }
  .brand-sub { display: block; font-size: 8px; letter-spacing: 11px; padding-left: 11px; margin-top: 8px; line-height: 1; }

  .title-pill { position: absolute; left: 459px; top: 208px; width: 285px; height: 40px;
    border-radius: 20px; background: var(--plum); display: flex; align-items: center; justify-content: center;
    font-family: "Montserrat", sans-serif; font-weight: 700; font-size: 12px; letter-spacing: 5.6px; padding-left: 5px; }

  .step { position: absolute; width: 160px; text-align: center; }
  .step-badge { display: block; width: 112px; height: 112px; margin: 0 auto; }
  .step-text { margin-top: 20px; font-family: "Arimo", sans-serif; font-size: 13.5px; line-height: 16px; }
  .step-num { font-weight: 700; }

  .col-1 { left: 351px; } .col-2 { left: 524px; } .col-3 { left: 697px; }
  .row-1 { top: 316px; } .row-2 { top: 547px; }
  .row-2 .step-text { margin-top: 22px; }
</style>
</head>
<body>
<main class="canvas">
  <header class="brand">
    <span class="brand-dot"></span>
    <span class="brand-name">TESSA</span>
    <span class="brand-sub">DINING</span>
  </header>

  <div class="title-pill">RESTAURANT PROCESS</div>

  <section class="step col-1 row-1">
    <svg class="step-badge" viewBox="0 0 112 112" aria-hidden="true">
      <circle cx="56" cy="56" r="56" fill="var(--plum)"/>
      <rect x="24" y="24" width="64" height="64" rx="7" fill="var(--ink)"/>
      <text x="56" y="61" text-anchor="middle" font-family="Montserrat, sans-serif" font-weight="800" font-size="10" letter-spacing="2" fill="var(--plum)">TESSA</text>
    </svg>
    <p class="step-text"><span class="step-num">1.</span> Host makes reservation and orders meal</p>
  </section>

  <section class="step col-2 row-1">
    <svg class="step-badge" viewBox="0 0 112 112" aria-hidden="true">
      <circle cx="56" cy="56" r="56" fill="var(--plum)"/>
      <path d="M84 43 A30 30 0 1 1 72 30" fill="none" stroke="var(--ink)" stroke-width="4" stroke-linecap="round"/>
      <path d="M43 57 L53 67 L72 46" fill="none" stroke="var(--ink)" stroke-width="5" stroke-linecap="round" stroke-linejoin="round"/>
    </svg>
    <p class="step-text"><span class="step-num">2.</span> Restaurant confirm reservation details</p>
  </section>

  <section class="step col-3 row-1">
    <svg class="step-badge" viewBox="0 0 112 112" aria-hidden="true">
      <circle cx="56" cy="56" r="56" fill="var(--plum)"/>
      <path d="M21 61 H73 L70 69 Q68 75 61 75 H28 Q22 75 21 68 Z" fill="var(--ink)"/>
      <path d="M72 64 Q82 58 102 57" fill="none" stroke="var(--ink)" stroke-width="4" stroke-linecap="round"/>
      <g fill="none" stroke="var(--ink)" stroke-width="2.2" stroke-linecap="round">
        <path d="M39 35 q-3 4 0 8 q3 4 0 8"/>
        <path d="M47 35 q-3 4 0 8 q3 4 0 8"/>
        <path d="M55 35 q-3 4 0 8 q3 4 0 8"/>
      </g>
    </svg>
    <p class="step-text"><span class="step-num">3.</span> Restaurant prepares cuisine and arranges cook/serve waiter</p>
  </section>

  <section class="step col-1 row-2">
    <svg class="step-badge" viewBox="0 0 112 112" role="img" aria-label="Chef hat pictogram between a fork and a knife">
      <circle cx="56" cy="56" r="56" fill="var(--plum)"/>
      <circle cx="56" cy="56" r="34" fill="var(--plum-soft)"/>
    </svg>
    <p class="step-text"><span class="step-num">4.</span> Cook/server arrive 1 hour before guests, prepares and sets table</p>
  </section>

  <section class="step col-2 row-2">
    <svg class="step-badge" viewBox="0 0 112 112" role="img" aria-label="Pictogram of a server carrying a dish">
      <circle cx="56" cy="56" r="56" fill="var(--plum)"/>
      <circle cx="56" cy="56" r="34" fill="var(--plum-soft)"/>
    </svg>
    <p class="step-text"><span class="step-num">5.</span> Cook/server cooks and serves meals and wine</p>
  </section>

  <section class="step col-3 row-2">
    <svg class="step-badge" viewBox="0 0 112 112" role="img" aria-label="Cheerful sparkling-clean pictogram">
      <circle cx="56" cy="56" r="56" fill="var(--plum)"/>
      <circle cx="56" cy="56" r="34" fill="var(--plum-soft)"/>
    </svg>
    <p class="step-text"><span class="step-num">6.</span> Cook/Server cleans up and finalises check with host</p>
  </section>
</main>
</body>
</html>
```